Business Cards & Letterhead
Birchway Family Chiropractic
Project: Business Cards & Letterhead
Business Cards & Letterhead - Health
Creative Brief
Professional
Dr. Melvin K. Tasker
Board Certified Atlas Orthogonist
4870 Harlow St. E, Suite 240 University Place, WA 98466
drtasker@birchwaychiro.com
birchwaychiro.com
Some design ideas: http://birchwaychiro.com/design/ideas.htm Interested in having cards done in black (possibly flat black) with logo, URL and name in glossy. Open to other ideas though too. Most of the letterhead will be printed on demand (black/white), but would also like to have a color representation of the letterhead.
Open to suggestions - needs to be light enough to write on and like the green fade - want to promote our URL too if possible. Should be non-glossy so pens will work well.

```html
<!DOCTYPE html>
<html lang="en">
<head>
<meta charset="utf-8">
<title>Birchway Family Chiropractic – Business Cards</title>
<link href="https://fonts.googleapis.com/css2?family=Arimo:wght@400;700&display=swap" rel="stylesheet">
<style>
  :root{
    --page:#ecebe8;
    --card-white:#ffffff;
    --card-black:#141414;
    --card-black-hi:#262626;
    --blue:#1f5fa6;
    --blue-dark:#17457c;
    --blue-bright:#3d86d6;
    --green:#7cbb2b;
    --green-light:#a9d45a;
    --ink:#333333;
    --ink-light:#cfcfcf;
  }
  *{box-sizing:border-box;margin:0;padding:0}
  html,body{width:1200px;height:932px;overflow:hidden}
  body{background:var(--page);font-family:"Arimo",Arial,sans-serif;position:relative}

  .card{position:absolute;width:520px;height:297px;border-radius:8px;overflow:hidden;box-shadow:0 6px 18px rgba(0,0,0,.18)}
  .card--white{background:var(--card-white)}
  .card--black{background:radial-gradient(ellipse at 40% 20%,var(--card-black-hi),var(--card-black) 70%)}
  .pos-front-white{left:50px;top:118px}
  .pos-front-black{left:630px;top:118px}
  .pos-back-white{left:50px;top:518px}
  .pos-back-black{left:630px;top:518px}

  .brand{position:absolute;display:flex;flex-direction:column;align-items:center;gap:8px}
  .brand__dot{width:34px;height:34px;border-radius:50%;background:var(--green);flex:none}
  .brand__name{font-size:20px;font-weight:400;letter-spacing:2px;text-transform:uppercase;color:var(--blue);line-height:1.15;text-align:center}
  .card--black .brand__name{color:var(--blue-bright)}
  .front .brand{left:28px;top:22px;width:250px}

  .person{position:absolute;left:34px;top:162px}
  .person__name{font-size:15px;font-weight:700;color:var(--blue)}
  .card--black .person__name{color:var(--blue-bright)}
  .person__title{font-size:8.5px;color:var(--ink);margin-top:3px}
  .card--black .person__title{color:var(--ink-light)}

  .contact{position:absolute;right:26px;top:146px;font-size:8.5px;line-height:1.45;color:var(--ink);text-align:left;width:170px}
  .card--black .contact{color:var(--ink-light)}
  .contact p + p{margin-top:8px}

  .swoosh{position:absolute;left:0;bottom:0;width:520px;height:80px}
  .url{position:absolute;left:34px;bottom:9px;font-size:9.5px;font-weight:700;color:#fff;letter-spacing:.3px}

  .back__fade{position:absolute;left:-10px;top:50px;width:260px;height:250px}
  .card--white .back__fade{background:radial-gradient(ellipse at 45% 45%,rgba(124,187,43,.18),rgba(31,95,166,.08) 55%,transparent 72%)}
  .card--black .back__fade{background:radial-gradient(ellipse at 45% 45%,rgba(255,255,255,.07),transparent 70%)}
  .back .brand{right:26px;top:142px;width:170px;gap:6px}
  .back .brand__name{font-size:11px;letter-spacing:1.5px}
  .back .url{left:auto;right:26px;bottom:40px;color:var(--blue);width:170px;text-align:center;font-size:8.5px}
  .card--black.back .url{color:var(--blue-bright)}
</style>
</head>
<body>

<section class="card card--white front pos-front-white" aria-label="Business card front, white">
  <div class="brand"><span class="brand__dot"></span><span class="brand__name">Birchway Family<br>Chiropractic</span></div>
  <div class="person">
    <div class="person__name">Dr. Melvin K. Tasker</div>
    <div class="person__title">Board Certified Atlas Orthogonist</div>
  </div>
  <div class="contact">
    <p>4870 Harlow St. E, Suite 240<br>Cedar Hollow, WA 98012</p>
    <p>Phone: (253) 555-0142<br>Fax: (253) 555-0187<br>Email: drtasker@birchwaychiro.com</p>
  </div>
  <svg class="swoosh" viewBox="0 0 520 80" preserveAspectRatio="none" aria-hidden="true">
    <path d="M0 50 C170 70 350 64 520 24 L520 80 L0 80 Z" fill="var(--green)"/>
    <path d="M0 60 C180 78 360 70 520 40 L520 80 L0 80 Z" fill="var(--blue)"/>
    <path d="M0 66 C180 82 360 76 520 56 L520 80 L0 80 Z" fill="var(--blue-dark)"/>
  </svg>
  <div class="url">www.birchwaychiro.com</div>
</section>

<section class="card card--black front pos-front-black" aria-label="Business card front, black">
  <div class="brand"><span class="brand__dot"></span><span class="brand__name">Birchway Family<br>Chiropractic</span></div>
  <div class="person">
    <div class="person__name">Dr. Melvin K. Tasker</div>
    <div class="person__title">Board Certified Atlas Orthogonist</div>
  </div>
  <div class="contact">
    <p>4870 Harlow St. E, Suite 240<br>Cedar Hollow, WA 98012</p>
    <p>Phone: (253) 555-0142<br>Fax: (253) 555-0187<br>Email: drtasker@birchwaychiro.com</p>
  </div>
  <svg class="swoosh" viewBox="0 0 520 80" preserveAspectRatio="none" aria-hidden="true">
    <path d="M0 50 C170 70 350 64 520 24 L520 80 L0 80 Z" fill="var(--green)"/>
    <path d="M0 60 C180 78 360 70 520 40 L520 80 L0 80 Z" fill="var(--blue)"/>
    <path d="M0 66 C180 82 360 76 520 56 L520 80 L0 80 Z" fill="var(--blue-dark)"/>
  </svg>
  <div class="url">www.birchwaychiro.com</div>
</section>

<section class="card card--white back pos-back-white" aria-label="Business card back, white">
  <div class="back__fade" role="img" aria-label="Faint enlarged brand mark as background decoration"></div>
  <div class="brand"><span class="brand__dot"></span><span class="brand__name">Birchway Family<br>Chiropractic</span></div>
  <div class="url">www.birchwaychiro.com</div>
</section>

<section class="card card--black back pos-back-black" aria-label="Business card back, black">
  <div class="back__fade" role="img" aria-label="Faint enlarged brand mark as background decoration"></div>
  <div class="brand"><span class="brand__dot"></span><span class="brand__name">Birchway Family<br>Chiropractic</span></div>
  <div class="url">www.birchwaychiro.com</div>
</section>

</body>
</html>
```